banner ad

We're looking for a banner similar to the one shown on the attached file. The same 4 keywords, the same text up top, but with new formatting, design and perhaps color scheme. Looking for something to catch people's attention that will stand out on this particular page shown in the attached image. Our goal is to find a banner with a better click through rate than the current version.

```html
<!DOCTYPE html>
<html lang="en">
<head>
<meta charset="utf-8">
<title>Blood Glucose Ad Unit</title>
<link rel="stylesheet" href="https://fonts.googleapis.com/css2?family=Poppins:wght@500;600;700&display=swap">
<style>
  :root {
    --header-bg: #0b3d4f;
    --header-accent: #19b4a6;
    --header-text: #ffffff;
    --label-text: #9fe3dc;
    --panel-bg: #f1f8f7;
    --panel-line: #d3e9e6;
    --button-top: #ff8a47;
    --button-bottom: #f2571c;
    --button-shadow: rgba(194, 66, 16, 0.35);
    --button-text: #ffffff;
    --arrow-bg: #ffffff;
    --arrow-fg: #f2571c;
  }

  * { box-sizing: border-box; margin: 0; padding: 0; }

  html, body {
    width: 1200px;
    height: 274px;
    overflow: hidden;
  }

  body {
    font-family: "Poppins", Arial, sans-serif;
    background: var(--panel-bg);
  }

  .ad-unit {
    position: relative;
    width: 1200px;
    height: 274px;
    background: var(--panel-bg);
    border-bottom: 2px solid var(--panel-line);
  }

  .ad-header {
    position: absolute;
    left: 0;
    top: 0;
    width: 1200px;
    height: 58px;
    display: flex;
    align-items: center;
    justify-content: space-between;
    padding: 0 28px;
    background: var(--header-bg);
    border-bottom: 4px solid var(--header-accent);
    color: var(--header-text);
  }

  .ad-title {
    font-size: 23px;
    font-weight: 600;
    line-height: 1;
  }

  .ad-label {
    font-size: 13px;
    font-weight: 600;
    letter-spacing: 1.5px;
    color: var(--label-text);
    border: 1.5px solid var(--label-text);
    border-radius: 14px;
    padding: 5px 14px 4px;
    line-height: 1;
  }

  .keyword-grid {
    position: absolute;
    left: 28px;
    top: 80px;
    width: 1144px;
    display: grid;
    grid-template-columns: 562px 562px;
    grid-template-rows: 76px 76px;
    column-gap: 20px;
    row-gap: 20px;
  }

  .keyword-button {
    display: flex;
    align-items: center;
    justify-content: space-between;
    padding: 0 14px 0 36px;
    border-radius: 38px;
    background: linear-gradient(to bottom, var(--button-top) 0%, var(--button-bottom) 100%);
    box-shadow: 0 5px 0 var(--button-shadow);
    color: var(--button-text);
    font-size: 24px;
    font-weight: 700;
    text-decoration: none;
    white-space: nowrap;
  }

  .keyword-arrow {
    flex: none;
    width: 50px;
    height: 50px;
    border-radius: 50%;
    background: var(--arrow-bg);
    display: flex;
    align-items: center;
    justify-content: center;
  }

  .keyword-arrow svg {
    width: 22px;
    height: 22px;
  }
</style>
</head>
<body>
  <section class="ad-unit">
    <header class="ad-header">
      <h1 class="ad-title">Ads related to blood glucose</h1>
      <span class="ad-label">ADVERTISEMENT</span>
    </header>
    <nav class="keyword-grid">
      <a class="keyword-button" href="#">Blood Glucose
        <span class="keyword-arrow"><svg viewBox="0 0 24 24" aria-hidden="true"><path d="M5 12h13M12 5l7 7-7 7" fill="none" stroke="#f2571c" stroke-width="3" stroke-linecap="round" stroke-linejoin="round"/></svg></span>
      </a>
      <a class="keyword-button" href="#">Blood Sugar Levels Chart
        <span class="keyword-arrow"><svg viewBox="0 0 24 24" aria-hidden="true"><path d="M5 12h13M12 5l7 7-7 7" fill="none" stroke="#f2571c" stroke-width="3" stroke-linecap="round" stroke-linejoin="round"/></svg></span>
      </a>
      <a class="keyword-button" href="#">Normal Blood Sugar Range
        <span class="keyword-arrow"><svg viewBox="0 0 24 24" aria-hidden="true"><path d="M5 12h13M12 5l7 7-7 7" fill="none" stroke="#f2571c" stroke-width="3" stroke-linecap="round" stroke-linejoin="round"/></svg></span>
      </a>
      <a class="keyword-button" href="#">What is Normal Blood Sugar
        <span class="keyword-arrow"><svg viewBox="0 0 24 24" aria-hidden="true"><path d="M5 12h13M12 5l7 7-7 7" fill="none" stroke="#f2571c" stroke-width="3" stroke-linecap="round" stroke-linejoin="round"/></svg></span>
      </a>
    </nav>
  </section>
</body>
</html>
```